Tulven Electrics Flyer Design Advertising

I am after an A5 Flyer design to help promote my electrical services business.
I would like to have information on what my business offers, photos of electrical work, and specials/deals for an amount of time.

Industry/Entity Type

Electrician

Font styles to use
Sans Serif

Colors
0292cd
33a6d7
85cae6
3176b5
333333
1b1b1b
ffffff
5c5c5c
474747

Requirements
Must have
• Specialising in New homes, renovations and commercial projects
• Contact details:
• ph. 0437 619 458
• email admin@tulvenelectrics.example.au
• facebook TulvenElectrics
• Specials/Deals:
• 10% off all electrical services
• or
• Free LED downlights on installation
• *Terms conditions apply
• ALL RESIDENTIAL & COMMERCIAL ELECTRICAL SERVICES
• - New Home installations
• - Commercial projects
• - Shop fit outs
• - Renovations
• - Smoke Detectors
• - Air Conditioning and Ceiling Fans
• - Garden Lighting
• - Oven and Cooktop Installations
• - Power Point installation
• - LED lighting upgrades
• - Security Lighting
• - Switchboard upgrades
• - Test and Tag
• - Commercial Property
• - General Electrical Maintenance

```html
<!DOCTYPE html>
<html lang="en">
<head>
<meta charset="utf-8">
<title>Tulven Electrics Flyer</title>
<link rel="stylesheet" href="https://fonts.googleapis.com/css2?family=Roboto+Condensed:wght@400;700&family=Open+Sans:ital,wght@0,400;0,700;1,400&display=swap">
<style>
  :root {
    --blue: #0292cd;
    --blue-mid: #33a6d7;
    --blue-light: #85cae6;
    --blue-deep: #3176b5;
    --ink: #333333;
    --ink-dark: #1b1b1b;
    --white: #ffffff;
    --grey: #5c5c5c;
    --grey-dark: #474747;
    --page-bg: #c9c9c9;
  }
  * { margin: 0; padding: 0; box-sizing: border-box; }
  html, body { width: 1200px; height: 687px; overflow: hidden; }
  body {
    background: var(--page-bg);
    font-family: "Open Sans", Arial, sans-serif;
    color: var(--ink);
  }
  .flyer {
    position: absolute;
    left: 370px; top: 19px;
    width: 460px; height: 649px;
    background: var(--white);
    overflow: hidden;
  }
  .rule { position: absolute; height: 5px; }
  .rule--dark { background: var(--ink); top: 12px; width: 132px; }
  .rule--blue { background: var(--blue); top: 22px; width: 104px; }
  .rule--left { left: 0; }
  .rule--right { right: 0; }

  .brand {
    position: absolute; left: 150px; top: 16px;
    display: flex; align-items: center; gap: 8px;
  }
  .brand__dot {
    width: 40px; height: 40px; border-radius: 50%;
    background: var(--blue);
  }
  .brand__name {
    font-family: "Roboto Condensed", Arial, sans-serif;
    font-weight: 700; font-size: 20px; color: var(--ink-dark);
    letter-spacing: 0.5px;
  }

  .headline {
    position: absolute; left: 16px; top: 86px;
    font-family: "Roboto Condensed", Arial, sans-serif;
    font-weight: 700; font-size: 26px; line-height: 26px;
    text-transform: uppercase;
  }
  .headline__accent { color: var(--blue); display: block; }
  .headline__main { color: var(--ink-dark); display: block; }

  .services {
    position: absolute; left: 16px; top: 168px;
    list-style: none; font-size: 11px; line-height: 14.6px; color: var(--ink-dark);
  }
  .services li { display: flex; align-items: center; gap: 3px; }
  .services svg { width: 9px; height: 9px; flex: none; }

  .portrait {
    position: absolute; left: 270px; top: 98px;
    width: 180px; height: 296px;
    background: linear-gradient(180deg, #e9e3de 0%, #2b3550 35%, #1e2538 100%);
    border-radius: 60px 60px 4px 4px;
  }

  .gallery {
    position: absolute; left: 0; top: 394px; width: 460px; height: 112px;
    background: linear-gradient(180deg, var(--blue-deep) 0%, var(--blue) 50%, var(--blue-deep) 100%);
  }
  .photo {
    position: absolute; border: 3px solid var(--white);
    box-shadow: 0 2px 5px rgba(0,0,0,.45);
  }
  .photo--house { left: 24px; top: 10px; width: 120px; height: 90px; transform: rotate(3deg);
    background: linear-gradient(180deg, #8fb3cf 0%, #dfe4e6 55%, #7a8a5a 100%); }
  .photo--pool { left: 166px; top: 10px; width: 120px; height: 88px; transform: rotate(-3deg);
    background: linear-gradient(180deg, #2a3550 0%, #c89a52 55%, #1d5a6b 100%); }
  .photo--interior { left: 316px; top: 8px; width: 124px; height: 92px; transform: rotate(3deg);
    background: linear-gradient(135deg, #f2f0ec 0%, #d8d2ca 55%, #b3582e 100%); }

  .specials {
    position: absolute; left: 0; top: 506px; width: 460px; height: 64px;
    background: var(--ink); color: var(--white); text-align: center;
  }
  .specials__title { font-size: 20px; font-weight: 400; margin-top: 9px; line-height: 22px; }
  .specials__offer { font-size: 11px; margin-top: 3px; }
  .specials__terms { font-size: 7px; font-style: italic; color: #bdbdbd; margin-top: 1px; }

  .tagline {
    position: absolute; left: 0; top: 571px; width: 460px; height: 38px;
    background: linear-gradient(180deg, #ececec 0%, var(--white) 40%, #e6e6e6 100%);
    border-top: 2px solid #d9d9d9;
    text-align: center; font-size: 11px; font-weight: 700; line-height: 36px;
    text-transform: uppercase; color: var(--ink-dark);
  }
  .tagline em { font-style: normal; color: var(--blue); }

  .contact {
    position: absolute; left: 0; top: 609px; width: 460px; height: 40px;
    background: var(--grey-dark); color: var(--white);
    display: flex; align-items: center; justify-content: space-between;
    padding: 0 34px 0 28px; font-size: 11px;
  }
  .contact__item { display: flex; align-items: center; gap: 4px; }
  .contact__item svg { width: 8px; height: 8px; }
  .contact__square { width: 7px; height: 7px; background: var(--blue); }
</style>
</head>
<body>
<main class="flyer">
  <div class="rule rule--dark rule--left"></div>
  <div class="rule rule--blue rule--left"></div>
  <div class="rule rule--dark rule--right"></div>
  <div class="rule rule--blue rule--right"></div>

  <div class="brand">
    <span class="brand__dot"></span>
    <span class="brand__name">Tulven Electrics</span>
  </div>

  <h1 class="headline">
    <span class="headline__accent">All Residential &amp;</span>
    <span class="headline__accent">Commercial</span>
    <span class="headline__main">Electrical Services</span>
  </h1>

  <ul class="services">
    <li><svg viewBox="0 0 10 10"><path d="M1 5l3 3 5-7" fill="none" stroke="#0292cd" stroke-width="2"/></svg>New Home installations</li>
    <li><svg viewBox="0 0 10 10"><path d="M1 5l3 3 5-7" fill="none" stroke="#0292cd" stroke-width="2"/></svg>Commercial projects</li>
    <li><svg viewBox="0 0 10 10"><path d="M1 5l3 3 5-7" fill="none" stroke="#0292cd" stroke-width="2"/></svg>Shop fit outs</li>
    <li><svg viewBox="0 0 10 10"><path d="M1 5l3 3 5-7" fill="none" stroke="#0292cd" stroke-width="2"/></svg>Renovations</li>
    <li><svg viewBox="0 0 10 10"><path d="M1 5l3 3 5-7" fill="none" stroke="#0292cd" stroke-width="2"/></svg>Smoke Detectors</li>
    <li><svg viewBox="0 0 10 10"><path d="M1 5l3 3 5-7" fill="none" stroke="#0292cd" stroke-width="2"/></svg>Air Conditioning and Ceiling Fans</li>
    <li><svg viewBox="0 0 10 10"><path d="M1 5l3 3 5-7" fill="none" stroke="#0292cd" stroke-width="2"/></svg>Garden Lighting</li>
    <li><svg viewBox="0 0 10 10"><path d="M1 5l3 3 5-7" fill="none" stroke="#0292cd" stroke-width="2"/></svg>Oven and Cooktop Installations</li>
    <li><svg viewBox="0 0 10 10"><path d="M1 5l3 3 5-7" fill="none" stroke="#0292cd" stroke-width="2"/></svg>Power Point Installation</li>
    <li><svg viewBox="0 0 10 10"><path d="M1 5l3 3 5-7" fill="none" stroke="#0292cd" stroke-width="2"/></svg>LED lighting upgrades</li>
    <li><svg viewBox="0 0 10 10"><path d="M1 5l3 3 5-7" fill="none" stroke="#0292cd" stroke-width="2"/></svg>Security Lighting</li>
    <li><svg viewBox="0 0 10 10"><path d="M1 5l3 3 5-7" fill="none" stroke="#0292cd" stroke-width="2"/></svg>Switchboard upgrades</li>
    <li><svg viewBox="0 0 10 10"><path d="M1 5l3 3 5-7" fill="none" stroke="#0292cd" stroke-width="2"/></svg>Test and Tag</li>
    <li><svg viewBox="0 0 10 10"><path d="M1 5l3 3 5-7" fill="none" stroke="#0292cd" stroke-width="2"/></svg>Commercial Property</li>
    <li><svg viewBox="0 0 10 10"><path d="M1 5l3 3 5-7" fill="none" stroke="#0292cd" stroke-width="2"/></svg>General Electrical Maintenance</li>
  </ul>

  <div class="portrait" role="img" aria-label="Smiling electrician in navy overalls and orange hard hat, arms crossed"></div>

  <section class="gallery">
    <div class="photo photo--house" role="img" aria-label="Two-storey white weatherboard house"></div>
    <div class="photo photo--pool" role="img" aria-label="Modern home with pool lit at dusk"></div>
    <div class="photo photo--interior" role="img" aria-label="Bright interior with pendant lights"></div>
  </section>

  <section class="specials">
    <h2 class="specials__title">SPECIALS/DEALS</h2>
    <p class="specials__offer">10% off all electrical services or Free LED downlights on installation</p>
    <p class="specials__terms">*Terms conditions apply</p>
  </section>

  <p class="tagline"><em>Specialising in New Homes,</em> Renovations and <em>Commercial Projects</em></p>

  <footer class="contact">
    <span class="contact__item"><svg viewBox="0 0 10 10"><path d="M2 1l2 2-1 1.5c.7 1.2 1.3 1.8 2.5 2.5L7 6l2 2-1.5 1.5C4.5 9 1 5.5.5 2.5z" fill="#33a6d7"/></svg>0437 619 458</span>
    <span class="contact__item"><svg viewBox="0 0 10 8"><rect x="0" y="0" width="10" height="8" fill="#33a6d7"/><path d="M0 0l5 4 5-4" fill="none" stroke="#474747" stroke-width="1"/></svg>admin@tulvenelectrics.example.au</span>
    <span class="contact__item"><span class="contact__square"></span>TulvenElectrics</span>
  </footer>
</main>
</body>
</html>
```